Business Consultancy Wordpress Design

Small business analysis consultancy.

Looking for a bold, clean design for Wordpress. Final site will only be a few pages, some contact information, services provided and a little background information. Potentially a blog.

Colours to be as per logo, with either black or white as the main colour.

Link is www.halvicadvisory.com

More details to be included in the best few days

Name - Halvic Consulting
Provides - Project Consultancy
Updates

Project Deadline Extended
Reason: I am going to be on holiday with little access to the web over 28/02 - 05/03 and am therefore extending the deadline

Target Market(s)

Business professionals

Industry/Entity Type

Business

Colors

Designer to choose colors to be used in the design.

Requirements
Must have
• Must contain the logo in the header
Footer must fit a 3 column layout in wordpress

Business style, royalty free stock images
Nice to have
• Would like the 1 or 2 column wordpress style layout
Should not have
• must not be blog or magazine style layout or look and feel

```html
<!DOCTYPE html>
<html lang="en">
<head>
<meta charset="utf-8">
<title>Halvic Consulting</title>
<link href="https://fonts.googleapis.com/css2?family=Michroma&family=Open+Sans:wght@400;600&display=swap" rel="stylesheet">
<style>
:root{
  --blue:#1e97d6;
  --blue-dark:#0b7dbd;
  --green:#5aa935;
  --green-dark:#3f8a22;
  --ink:#3a3a3a;
  --muted:#666;
  --light:#ececec;
  --pale:#f4f6fb;
  --footer:#e3e7ef;
  --line:#cfd3da;
}
*{margin:0;padding:0;box-sizing:border-box}
html,body{width:720px;height:1200px;overflow:hidden}
body{position:relative;font-family:"Open Sans",Arial,sans-serif;color:var(--ink);background:var(--pale)}
.abs{position:absolute}
.wide{font-family:"Michroma","Open Sans",sans-serif}

.top-strip{left:0;top:0;width:720px;height:5px;background:#ddd}
.header{left:0;top:5px;width:720px;height:66px;background:#fff}
.brand{left:43px;top:28px;display:flex;align-items:center;gap:8px;font-size:14px;color:#555;letter-spacing:.2px}
.brand-dot{width:22px;height:22px;border-radius:50%;background:var(--blue)}
.socials{left:612px;top:25px;display:flex;gap:5px}
.socials span{width:17px;height:17px;border-radius:50%;background:var(--blue-dark)}
.phone{left:556px;top:47px;display:flex;align-items:center;gap:6px;font-size:13px;color:#555;letter-spacing:1.5px}

.nav{left:0;top:71px;width:720px;height:34px;background:linear-gradient(#34aee6,#0e8cd0)}
.nav a{position:absolute;top:0;height:34px;line-height:34px;font-size:8.5px;letter-spacing:1.5px;color:#fff;text-decoration:none}
.nav a.active{background:#0d6fa8;padding:0 4px}
.search{left:556px;top:6px;width:127px;height:20px;background:#fff;border-radius:2px;font-size:7.5px;color:#999;padding:5px 6px;letter-spacing:.5px}
.search svg{position:absolute;right:5px;top:4px}

.hero{left:0;top:105px;width:720px;height:221px;background:linear-gradient(180deg,#cfd8e0 0%,#9aa6b0 45%,#c8d0d6 75%,#eef1f4 100%)}
.welcome{left:110px;top:62px;width:270px;height:38px;background:rgba(60,60,60,.55);text-align:center;padding-top:6px}
.welcome small{display:block;font-size:8.5px;color:#fff;letter-spacing:2px}
.welcome strong{display:block;font-weight:400;font-size:14px;color:var(--blue);letter-spacing:2px;line-height:16px}
.quick{left:470px;top:13px;width:213px;height:208px;background:rgba(70,70,70,.85);padding:15px 20px}
.quick h3{font-weight:400;font-size:12.5px;color:#fff;letter-spacing:1px;margin-bottom:8px}
.field{width:165px;height:22px;background:#fff;margin-bottom:5px;font-size:9.5px;color:#666;padding:4px 7px;letter-spacing:.8px}
.field.msg{height:60px;margin-top:1px}
.send{width:165px;height:22px;margin-top:7px;background:linear-gradient(#6dbf45,var(--green-dark));color:#fff;font-size:9.5px;letter-spacing:1px;display:flex;align-items:center;justify-content:center;gap:5px}

.section-title{left:43px;width:624px;text-align:center;font-size:12px;color:var(--blue);letter-spacing:1.5px}
.section-title b{color:var(--green);font-weight:400}
.rule{left:43px;width:624px;height:1px;background:var(--line)}
.mark{width:12px;height:12px;border-radius:50%;background:var(--green);left:349px}

.what{left:0;top:326px;width:720px;height:276px;background:var(--light)}
.service{width:170px;text-align:center}
.service h4{font-size:7.5px;font-weight:400;letter-spacing:1px;color:#333;margin:8px 0 6px}
.service p{font-size:9.5px;line-height:13px;color:var(--muted);letter-spacing:.6px}
.service a{display:block;margin-top:5px;font-size:7.5px;color:var(--blue);letter-spacing:1px;text-decoration:none}
.btn{width:96px;height:20px;background:linear-gradient(#67b83f,var(--green-dark));color:#fff;font-size:7.5px;letter-spacing:.8px;text-align:center;line-height:20px;border:1px solid #3a7f20}

.about-text{left:86px;top:670px;width:551px;text-align:center;font-size:9.5px;line-height:17.6px;color:var(--muted);letter-spacing:.8px}
.member{width:100px;text-align:center}
.avatar{width:66px;height:66px;border-radius:50%;margin:0 auto;border:3px solid #d6d6d6;background:radial-gradient(circle at 50% 40%,#c9b7a5,#6f7680)}
.member h5{font-weight:400;font-size:7.5px;letter-spacing:1px;color:#444;margin-top:10px}
.member span{font-size:6.5px;color:var(--blue);letter-spacing:.8px}

.newsletter{left:121px;top:937px;width:501px;height:60px;background:linear-gradient(90deg,#0c85cf,#1d9be0);border:1px solid #0a6ea8}
.newsletter .inner{position:absolute;left:6px;top:6px;right:6px;bottom:6px;border:1px solid rgba(255,255,255,.35)}
.mailbox{left:130px;top:912px;width:56px;height:73px;border-radius:22px 22px 4px 4px;background:linear-gradient(#2a9be0,#0a5ea0)}
.nl-title{left:198px;top:946px;font-size:7.5px;color:#fff;letter-spacing:1px}
.nl-input{left:198px;top:961px;width:314px;height:20px;background:#fff;font-size:9px;color:#888;padding:4px 12px;letter-spacing:1px}
.nl-btn{left:523px;top:961px;width:80px;height:20px;background:linear-gradient(#6dbf45,var(--green-dark));color:#fff;font-size:7.5px;letter-spacing:1px;text-align:center;line-height:20px}

.footer{left:0;top:1030px;width:720px;height:144px;background:var(--footer)}
.f-title{font-size:9px;color:var(--blue);letter-spacing:1px}
.f-rule{height:1px;background:#b9bec7}
.blog-img{left:41px;top:1086px;width:94px;height:66px;border:3px solid #333;background:linear-gradient(#e8ecef,#b8c0c8)}
.blog-body{left:141px;top:1085px;width:150px;font-size:8.5px;line-height:9.5px;color:#555;letter-spacing:.6px;text-align:justify}
.blog-body h6{font-weight:400;font-size:9.5px;color:#444;letter-spacing:.8px;margin-bottom:3px;text-align:left}
.blog-body a{display:block;margin-top:6px;color:var(--blue);text-decoration:none}
.f-list{list-style:none;font-size:9.5px;color:#444;letter-spacing:.8px}
.f-list li{display:flex;align-items:center;gap:6px;height:21px}
.f-list .ico{width:16px;height:16px;border-radius:50%;background:var(--blue-dark)}
.links{display:grid;grid-template-columns:67px 60px;row-gap:7px;font-size:9.5px;color:#444;letter-spacing:.8px}
.links span::before{content:"›";color:var(--blue);font-weight:600;font-size:13px;margin-right:4px}
.bottom{left:0;top:1174px;width:720px;height:26px;background:var(--blue);color:#fff;font-size:6px;letter-spacing:1px;text-align:center;line-height:26px}
</style>
</head>
<body>
<div class="abs top-strip"></div>

<header class="abs header">
  <div class="abs brand"><span class="brand-dot"></span>Halvic Consulting</div>
  <div class="abs socials"><span></span><span></span><span></span></div>
  <div class="abs phone">
    <svg width="12" height="12" viewBox="0 0 12 12"><rect width="12" height="12" rx="2" fill="#1e97d6"/><path d="M4 3c-.6.6-.6 2 1 3.6S8.4 8.6 9 8l-1.2-1.2-.9.6-1.8-1.8.6-.9z" fill="#fff"/></svg>
    02-9876-5432
  </div>
</header>

<nav class="abs nav">
  <a class="active wide" style="left:43px">HOME</a>
  <a class="wide" style="left:118px">ABOUT</a>
  <a class="wide" style="left:195px">SERVICES</a>
  <a class="wide" style="left:291px">BLOG</a>
  <a class="wide" style="left:360px">CONTACT</a>
  <div class="abs search">Keyword Search...
    <svg width="12" height="12" viewBox="0 0 12 12"><circle cx="5" cy="5" r="3.5" fill="none" stroke="#aaa" stroke-width="1.4"/><path d="M7.5 7.5 11 11" stroke="#aaa" stroke-width="1.6"/></svg>
  </div>
</nav>

<section class="abs hero" role="img" aria-label="Blurred photo of business people standing by a bright office window">
  <div class="abs welcome"><small class="wide">WELCOME TO</small><strong class="wide">HALVIC CONSULTING</strong></div>
  <form class="abs quick">
    <h3>Quick Contact Form</h3>
    <div class="field">Firstname</div>
    <div class="field">Email Address</div>
    <div class="field msg">Message...</div>
    <div class="send">SEND MESSAGE
      <svg width="11" height="11" viewBox="0 0 11 11"><rect x=".7" y="2" width="8" height="8" fill="none" stroke="#fff" stroke-width="1.2"/><path d="M2.5 5.5 4.5 7.5 10 1" fill="none" stroke="#fff" stroke-width="1.5"/></svg>
    </div>
  </form>
</section>

<section class="abs what">
  <h2 class="abs section-title wide" style="top:28px">WHAT <b>WE</b> DO</h2>
  <div class="abs rule" style="top:51px"></div>
  <div class="abs mark" style="top:45px"></div>

  <div class="abs service" style="left:84px;top:92px">
    <svg width="46" height="32" viewBox="0 0 46 32"><circle cx="12" cy="20" r="10" fill="#2c3540"/><circle cx="34" cy="20" r="10" fill="#2c3540"/><rect x="16" y="8" width="14" height="10" rx="3" fill="#2c3540"/><circle cx="12" cy="21" r="5.5" fill="#2a9ad6"/><circle cx="34" cy="21" r="5.5" fill="#2a9ad6"/></svg>
    <h4 class="wide">PROJECT SCOPING</h4>
    <p>Lorem ipsum dolor sit amet, consectetur adipiscing elit. Ut felis ligula, dignissim sit amet</p>
    <a class="wide">READ MORE ›</a>
  </div>
  <div class="abs service" style="left:275px;top:92px">
    <svg width="40" height="32" viewBox="0 0 40 32"><rect x="14" y="1" width="12" height="7" rx="2" fill="none" stroke="#2c3540" stroke-width="2.5"/><rect x="2" y="7" width="36" height="24" rx="3" fill="#2c3540"/><rect x="6" y="14" width="28" height="10" fill="#2a9ad6"/><rect x="9" y="13" width="4" height="12" fill="#2c3540"/><rect x="27" y="13" width="4" height="12" fill="#2c3540"/></svg>
    <h4 class="wide">METHODS &amp; APPROACH</h4>
    <p>Lorem ipsum dolor sit amet, consectetur adipiscing elit. Ut felis ligula, dignissim sit amet</p>
    <a class="wide">READ MORE ›</a>
  </div>
  <div class="abs service" style="left:473px;top:92px">
    <svg width="36" height="32" viewBox="0 0 36 32"><ellipse cx="14" cy="5" rx="11" ry="4" fill="#2c3540"/><rect x="3" y="7" width="22" height="6" rx="2" fill="#2c3540"/><rect x="3" y="15" width="22" height="6" rx="2" fill="#2c3540"/><rect x="3" y="23" width="22" height="6" rx="2" fill="#2c3540"/><path d="M25 14v16M17 22h16" stroke="#2a9ad6" stroke-width="5"/></svg>
    <h4 class="wide">ISSUE &amp; RISK MANAGEMENT</h4>
    <p>Lorem ipsum dolor sit amet, consectetur adipiscing elit. Ut felis ligula, dignissim sit amet</p>
    <a class="wide">READ MORE ›</a>
  </div>

  <div class="abs btn" style="left:316px;top:228px">View our services</div>
</section>

<h2 class="abs section-title wide" style="top:620px">WHO <b>WE</b> ARE</h2>
<div class="abs rule" style="top:645px"></div>
<div class="abs mark" style="top:639px"></div>
<p class="abs about-text">Lorem ipsum dolor sit amet, consectetur adipiscing elit. Ut felis ligula, dignissim sit amet interdum non, lobortis eget lacus. Nulla ultricies at eros non auctor. Donec elementum ante vel eros tempus blandit. Phasellus condimentum mollis pellentesque.</p>

<div class="abs member" style="left:145px;top:752px"><div class="avatar" role="img" aria-label="Portrait photo of team member"></div><h5 class="wide">ALAN REED GRANT</h5><span class="wide">POSITION</span></div>
<div class="abs member" style="left:255px;top:752px"><div class="avatar" role="img" aria-label="Portrait photo of team member"></div><h5 class="wide">PETER HOLLIS</h5><span class="wide">POSITION</span></div>
<div class="abs member" style="left:364px;top:752px"><div class="avatar" role="img" aria-label="Portrait photo of team member"></div><h5 class="wide">SAM CARVER</h5><span class="wide">POSITION</span></div>
<div class="abs member" style="left:473px;top:752px"><div class="avatar" role="img" aria-label="Portrait photo of team member"></div><h5 class="wide">NEIL BARROW</h5><span class="wide">POSITION</span></div>

<div class="abs btn" style="left:316px;top:878px">View our team</div>

<div class="abs newsletter"><div class="inner"></div></div>
<div class="abs mailbox" role="img" aria-label="Illustration of a blue mailbox"></div>
<div class="abs nl-title wide">JOIN TO OUR NEWSLETTER</div>
<div class="abs nl-input">Email address</div>
<div class="abs nl-btn wide">JOIN NOW!</div>

<footer class="abs footer">
  <h3 class="abs f-title wide" style="left:40px;top:25px">FROM OUR BLOG</h3>
  <div class="abs f-rule" style="left:40px;top:44px;width:232px"></div>
  <h3 class="abs f-title wide" style="left:318px;top:25px">CONNECT WITH US</h3>
  <div class="abs f-rule" style="left:312px;top:44px;width:154px"></div>
  <h3 class="abs f-title wide" style="left:547px;top:25px">QUICKLINKS</h3>
  <div class="abs f-rule" style="left:540px;top:44px;width:154px"></div>

  <ul class="abs f-list" style="left:324px;top:52px">
    <li><span class="ico"></span>Our Chatterly page</li>
    <li><span class="ico"></span>Our Friendhub page</li>
    <li><span class="ico"></span>Our Workweb page</li>
  </ul>
  <div class="abs links" style="left:544px;top:55px">
    <span>Home</span><span>Blog</span><span>About</span><span>Contact</span><span>Services</span>
  </div>
</footer>
<div class="abs blog-img" role="img" aria-label="Photo of a presenter pointing at a growth chart for an audience"></div>
<div class="abs blog-body">
  <h6>BLOG TITLE GOES HERE</h6>
  Lorem ipsum dolor sit amet, consectetur adipiscing elit consectetur adipiscing elitconsectetur adipiscing elit adipiscing
  <a>more &gt;&gt;</a>
</div>

<div class="abs bottom wide">COPYRIGHT © 2014 HALVIC CONSULTANCY</div>
</body>
</html>
```